Data Visualization (graphs, tables, models, circles)

We need an intuitive - user friendly - and fresh design line for our data visualization.

You know. Keep The Path Clear!

Our core product is based on the presentation and interpretation of different data sources that we combine into graphs, tables, charts etc and make visible to clients through a web platform and or Reports. Our business area is Search & Social Media Intelligence.

See Trevla.com for some inspiration in terms of current colors and a better understanding of the company. Our Logo / Name is the only one thing that cannot be changed. Everything else is up to you. Feel free to ask questions.

I have attached a few screenshots of some of our features and as you can see - there has never been a designer on this assignment. We are looking for a long term relationship with a designer that can work with us on an ongoing basis.

Design of graphs/models/circles/tables needs to be able to fit into Infographics also.

We are basically looking for an identity for our data visualization. Meaning that readers / target audience can recognize our graphs and say: Check out the cool graphs by Trevla :-)

Think: Zorbix, PlumLedger, etc. in terms of data presentation.
Updates

Project Deadline Extended
Reason: Due to illness we lost a few days last week and have not have sufficient time to look through the different designs.

Target Market(s)

Marketing People, CEO's, Strategic Planners, Ad Agencies, Decision Makers

Industry/Entity Type

Business

Requirements
Must have
• Must present at least 1 line graph (like file 1 and 2), 1 pie chart, 1 column graph and 1 matrix (like file3).

```html
<!DOCTYPE html>
<html lang="en">
<head>
<meta charset="utf-8">
<title>Trevla — Column Graph</title>
<link rel="stylesheet" href="https://fonts.googleapis.com/css2?family=Ubuntu:wght@500&family=Tinos&family=Open+Sans:wght@400&display=swap">
<style>
  :root {
    --bg-light: #ffffff;
    --bg-mid: #f4f4f4;
    --bg-shade: #e6e6e6;
    --brand-red: #9b1116;
    --title-black: #111111;
    --title-blue: #0a0aff;
    --bar-green: #6a8a1d;
    --axis: #111111;
    --label: #222222;
  }
  html, body {
    margin: 0;
    padding: 0;
    overflow: hidden;
  }
  .canvas {
    position: relative;
    width: 1200px;
    height: 1000px;
    overflow: hidden;
    background: radial-gradient(ellipse at 35% 35%, var(--bg-light) 0%, var(--bg-mid) 55%, var(--bg-shade) 100%);
  }
  .backdrop {
    position: absolute;
    inset: 0;
  }
  .brand-name {
    position: absolute;
    left: 0;
    width: 1280px;
    top: 14px;
    margin: 0;
    text-align: center;
    font-family: "Ubuntu", sans-serif;
    font-weight: 500;
    font-size: 86px;
    line-height: 1;
    color: var(--brand-red);
  }
  .chart-title {
    position: absolute;
    left: 0;
    width: 1250px;
    top: 124px;
    margin: 0;
    text-align: center;
    font-family: "Tinos", serif;
    font-weight: 400;
    font-size: 65px;
    line-height: 1;
    color: var(--title-black);
  }
  .chart-title .chart-type { color: var(--title-blue); }
  .column-chart {
    position: absolute;
    inset: 0;
  }
  .column-chart text {
    font-family: "Open Sans", sans-serif;
    font-size: 13px;
    fill: var(--label);
  }
  .column-chart .bar { fill: var(--bar-green); }
  .column-chart .axis { stroke: var(--axis); stroke-width: 2; fill: none; }
  .column-chart .tick { stroke: var(--axis); stroke-width: 1.5; }
</style>
</head>
<body>
<div class="canvas">
  <div class="backdrop" role="img" aria-label="Soft grey background with a faint abstract swirl"></div>

  <h1 class="brand-name">Trevla</h1>
  <h2 class="chart-title">A. <span class="chart-type">Column Graph</span></h2>

  <svg class="column-chart" viewBox="0 0 1200 1000" role="img" aria-label="Column graph of monthly returns in 2012">
    <g class="y-axis-title">
      <text x="53" y="214">Your</text>
      <text x="53" y="234">Returns</text>
      <text x="53" y="254">(€. million.)</text>
    </g>

    <g class="bars">
      <rect class="bar" x="137.5" y="356.1" width="31" height="410.9"/>
      <rect class="bar" x="221.5" y="338.8" width="31" height="428.2"/>
      <rect class="bar" x="304.5" y="660.6" width="31" height="106.4"/>
      <rect class="bar" x="393.5" y="484.8" width="31" height="282.2"/>
      <rect class="bar" x="477.5" y="392.3" width="31" height="374.7"/>
      <rect class="bar" x="560.5" y="544.2" width="31" height="222.8"/>
      <rect class="bar" x="647.5" y="517.0" width="31" height="250.0"/>
      <rect class="bar" x="732.5" y="687.8" width="31" height="79.2"/>
      <rect class="bar" x="813.5" y="625.9" width="31" height="141.1"/>
      <rect class="bar" x="901.5" y="291.8" width="31" height="475.2"/>
      <rect class="bar" x="987.5" y="541.8" width="31" height="225.2"/>
      <rect class="bar" x="1069.5" y="514.5" width="31" height="252.5"/>
    </g>

    <path class="axis" d="M111 272 V767 H1149"/>

    <g class="y-ticks">
      <line class="tick" x1="104" y1="767" x2="111" y2="767"/>
      <line class="tick" x1="104" y1="717.5" x2="111" y2="717.5"/>
      <line class="tick" x1="104" y1="668" x2="111" y2="668"/>
      <line class="tick" x1="104" y1="618.5" x2="111" y2="618.5"/>
      <line class="tick" x1="104" y1="569" x2="111" y2="569"/>
      <line class="tick" x1="104" y1="519.5" x2="111" y2="519.5"/>
      <line class="tick" x1="104" y1="470" x2="111" y2="470"/>
      <line class="tick" x1="104" y1="420.5" x2="111" y2="420.5"/>
      <line class="tick" x1="104" y1="371" x2="111" y2="371"/>
      <line class="tick" x1="104" y1="321.5" x2="111" y2="321.5"/>
      <line class="tick" x1="104" y1="272" x2="111" y2="272"/>
    </g>
    <g class="y-labels" text-anchor="end">
      <text x="97" y="772">0</text>
      <text x="97" y="722">1</text>
      <text x="97" y="673">2</text>
      <text x="97" y="623">3</text>
      <text x="97" y="574">4</text>
      <text x="97" y="524">5</text>
      <text x="97" y="475">6</text>
      <text x="97" y="425">7</text>
      <text x="97" y="376">8</text>
      <text x="97" y="326">9</text>
      <text x="97" y="277">10</text>
    </g>

    <g class="x-ticks">
      <line class="tick" x1="111" y1="767" x2="111" y2="774"/>
      <line class="tick" x1="195" y1="767" x2="195" y2="774"/>
      <line class="tick" x1="278" y1="767" x2="278" y2="774"/>
      <line class="tick" x1="365" y1="767" x2="365" y2="774"/>
      <line class="tick" x1="451" y1="767" x2="451" y2="774"/>
      <line class="tick" x1="535" y1="767" x2="535" y2="774"/>
      <line class="tick" x1="620" y1="767" x2="620" y2="774"/>
      <line class="tick" x1="706" y1="767" x2="706" y2="774"/>
      <line class="tick" x1="789" y1="767" x2="789" y2="774"/>
      <line class="tick" x1="873" y1="767" x2="873" y2="774"/>
      <line class="tick" x1="960" y1="767" x2="960" y2="774"/>
      <line class="tick" x1="1044" y1="767" x2="1044" y2="774"/>
      <line class="tick" x1="1127" y1="767" x2="1127" y2="774"/>
    </g>
    <g class="x-labels" text-anchor="middle">
      <text x="150" y="790">January</text>
      <text x="237" y="790">February</text>
      <text x="320" y="790">March</text>
      <text x="409" y="790">April</text>
      <text x="494" y="790">May</text>
      <text x="576" y="790">June</text>
      <text x="663" y="790">July</text>
      <text x="748" y="790">August</text>
      <text x="840" y="790">September</text>
      <text x="917" y="790">October</text>
      <text x="1005" y="790">November</text>
      <text x="1087" y="790">December</text>
    </g>
    <text class="x-axis-title" x="679" y="813" text-anchor="middle">Months (year 2012)</text>
  </svg>
</div>
</body>
</html>
```